Criação de Power Point Slide Mestre para Advocacia e Direito
" Samos uma empresa especializada em cobrança condominial, cobramos taxas condominiais em atraso. Garantimos a receita mensal do condomínio para que não haja inadimplência, damos andamentos em abertura de processos judiciais. "

```html
<!DOCTYPE html>
<html lang="pt-BR">
<head>
<meta charset="utf-8">
<title>Cobrança Condominial — Portal do Condômino</title>
<link rel="stylesheet" href="https://fonts.googleapis.com/css2?family=Montserrat:wght@400;500;700;800&display=swap">
<style>
  :root {
    --white: #ffffff;
    --panel: #6e6e70;
    --orange: #cf5527;
    --orange-soft: #e07a4c;
    --label: #f4f4f4;
    --photo-left-a: #4a4744;
    --photo-left-b: #8c7a6e;
    --photo-right-a: #9aa7b1;
    --photo-right-b: #e6ebee;
  }
  * { margin: 0; padding: 0; box-sizing: border-box; }
  html, body { width: 1200px; height: 1200px; overflow: hidden; background: var(--white); }
  body { position: relative; font-family: "Montserrat", sans-serif; }

  .slide-master { position: absolute; left: 0; top: 259px; width: 1200px; height: 677px; }
  .photo-client {
    position: absolute; left: 0; top: 0; width: 259px; height: 100%;
    background: linear-gradient(160deg, var(--photo-left-b) 0%, var(--photo-left-a) 70%);
  }
  .photo-building {
    position: absolute; right: 0; top: 0; width: 259px; height: 100%;
    background: linear-gradient(200deg, var(--photo-right-a) 0%, var(--photo-right-b) 80%);
  }
  .services-panel {
    position: absolute; left: 259px; top: 0; width: 682px; height: 100%;
    background: var(--panel);
  }

  .service { position: absolute; width: 230px; text-align: center; }
  .service-tile { position: relative; width: 230px; height: 140px; background: var(--orange); }
  .service-icon {
    position: absolute; left: 70px; top: 14px; width: 90px; height: 78px;
    background: var(--orange-soft); border-radius: 10px;
  }
  .service-title {
    position: absolute; left: 0; right: 0; bottom: 10px;
    color: var(--white); font-weight: 800; font-size: 17px; white-space: nowrap;
  }
  .service-caption {
    margin-top: 12px; color: var(--label); font-weight: 500; font-size: 17px; white-space: nowrap;
  }

  .service-chamados   { left: 72px;  top: 43px; }
  .service-comunicado { left: 383px; top: 43px; }
  .service-pendencias { left: 72px;  top: 259px; }
  .service-reservas   { left: 383px; top: 259px; }
  .service-documentos { left: 226px; top: 471px; }

  .action-bar {
    position: absolute; left: 89px; top: 661px; width: 504px; height: 12px;
    background: var(--orange); border-radius: 6px;
  }
</style>
</head>
<body>
  <section class="slide-master">
    <div class="photo-client" role="img" aria-label="Foto de condômino sorridente consultando o celular"></div>
    <div class="services-panel">
      <div class="service service-chamados">
        <div class="service-tile">
          <div class="service-icon" role="img" aria-label="Ícone de balões de conversa"></div>
          <div class="service-title">Chamados</div>
        </div>
        <p class="service-caption">Ver e abrir chamados</p>
      </div>
      <div class="service service-comunicado">
        <div class="service-tile">
          <div class="service-icon" role="img" aria-label="Ícone de megafone"></div>
          <div class="service-title">Comunicado</div>
        </div>
        <p class="service-caption">Visualizar comunicados</p>
      </div>
      <div class="service service-pendencias">
        <div class="service-tile">
          <div class="service-icon" role="img" aria-label="Ícone de boletos de taxa condominial em atraso"></div>
          <div class="service-title">Minhas Pendências</div>
        </div>
        <p class="service-caption">Cosultar Pendências</p>
      </div>
      <div class="service service-reservas">
        <div class="service-tile">
          <div class="service-icon" role="img" aria-label="Ícone de calendário com data marcada"></div>
          <div class="service-title">Reservas</div>
        </div>
        <p class="service-caption">Reservar Espaços</p>
      </div>
      <div class="service service-documentos">
        <div class="service-tile">
          <div class="service-icon" role="img" aria-label="Ícone de computador com documentos processuais"></div>
          <div class="service-title">Documentos</div>
        </div>
        <p class="service-caption">Visualizar Documentos</p>
      </div>
      <div class="action-bar"></div>
    </div>
    <div class="photo-building" role="img" aria-label="Foto de edifício residencial moderno de vidro"></div>
  </section>
</body>
</html>
```